Werbebrief
Zielgruppe
Unsere Zielgruppe sind Geschäftsführer junger Unternehmen.
Hallo,
Wir benötigen einen "Werbebrief". Es ist jedoch weniger ein Brief, als viel mehr eine etwas größerer "Werbekarte" (diese soll 105 x 210mm groß sein).
Auf der Vorderseite soll folgender Text stehen:
Für Unternehmen, die gerne expandieren möchten
Auf der Rückseite soll folgender Link stehen:
www.tessaro-werk.de/Expandieren
Darunter soll folgendes stehen:
Ihr persönlicher Code: ABC123
Wichtig ist, dass wir den Code individuell ändern können, da jeder einen anderen Code bekommt.
Unser Logo und Corporate Farbe habe ich hochgeladen. Das Design sollte auf jeden Fall zu unserer Webseite passen (www.tessaro-werk.de)
Wir freuen uns auf Ihre Vorschläge.

```html
<!DOCTYPE html>
<html lang="de">
<head>
<meta charset="utf-8">
<title>Tessaro Werk – Werbekarte</title>
<link rel="stylesheet" href="https://fonts.googleapis.com/css2?family=Ubuntu:wght@300;400&display=swap">
<style>
  :root {
    --page-bg: #e9e6e1;
    --card-light: #2b58a3;
    --card-dark: #1d4187;
    --ink: #ffffff;
    --ink-soft: rgba(255,255,255,0.92);
    --rule-strong: rgba(255,255,255,0.95);
    --rule-faint: rgba(255,255,255,0.28);
  }
  * { margin: 0; padding: 0; box-sizing: border-box; }
  html, body {
    width: 1200px; height: 1200px; overflow: hidden;
    background: var(--page-bg);
    font-family: "Ubuntu", sans-serif;
    color: var(--ink);
  }
  .sheet {
    position: relative; width: 1200px; height: 1200px;
  }
  .card {
    position: absolute; left: 100px; width: 1000px; height: 500px;
    background: linear-gradient(180deg, var(--card-light) 0%, #244c98 55%, var(--card-dark) 100%);
    box-shadow: 0 10px 30px rgba(0,0,0,0.25);
    overflow: hidden;
  }
  .card--front { top: 70px; }
  .card--back { top: 630px; }

  .brand {
    position: absolute; top: 34px; right: 44px;
    display: flex; align-items: center; gap: 12px;
    font-weight: 400; font-size: 30px; letter-spacing: 0.2px;
    color: var(--ink);
  }
  .brand__dot {
    width: 14px; height: 14px; border-radius: 50%; background: var(--ink);
  }

  .rule {
    position: absolute; left: 0; width: 100%; height: 3px;
  }
  .rule--strong {
    background: linear-gradient(90deg, rgba(255,255,255,0.55) 0%, var(--rule-strong) 40%, var(--rule-strong) 75%, rgba(255,255,255,0.6) 100%);
  }
  .rule--faint {
    height: 2px;
    background: linear-gradient(90deg, transparent 0%, var(--rule-faint) 30%, rgba(255,255,255,0.45) 60%, transparent 100%);
  }

  .headline {
    position: absolute; left: 0; right: 0; top: 250px;
    text-align: center; font-weight: 300; font-size: 44px; line-height: 1.22;
    padding-left: 120px;
  }

  .code {
    position: absolute; left: 60px; top: 110px;
    font-weight: 300; font-size: 38px;
  }
  .note {
    position: absolute; right: 90px; top: 280px; width: 380px;
    text-align: right; font-weight: 300; font-size: 20px; line-height: 1.3;
    color: var(--ink-soft);
  }
  .url {
    position: absolute; right: 50px; bottom: 40px;
    font-weight: 300; font-size: 38px; letter-spacing: 0.3px;
  }
</style>
</head>
<body>
<main class="sheet">
  <section class="card card--front" aria-label="Vorderseite">
    <div class="brand"><span class="brand__dot"></span><span class="brand__name">Tessaro Werk</span></div>
    <div class="rule rule--faint" style="top:150px"></div>
    <div class="rule rule--strong" style="top:232px"></div>
    <h1 class="headline">Für Unternehmen, die gerne<br>expandieren möchten</h1>
    <div class="rule rule--faint" style="top:405px"></div>
  </section>

  <section class="card card--back" aria-label="Rückseite">
    <div class="brand"><span class="brand__dot"></span><span class="brand__name">Tessaro Werk</span></div>
    <p class="code">Ihr persönlicher Code: Tes1612</p>
    <div class="rule rule--strong" style="top:170px"></div>
    <div class="rule rule--faint" style="top:255px"></div>
    <p class="note">Wichtig ist, dass wir den Code individuell ändern können, da jeder einen anderen Code bekommt.</p>
    <div class="rule rule--strong" style="top:385px"></div>
    <p class="url">www.tessaro-werk.de/Expandieren</p>
  </section>
</main>
</body>
</html>
```